Medical centre needs a business card

We are a medcial centre in Australia, needing a new business card. Our demographic is low working class families. We are going to be renovating our premises to modernise the look and also had a new logo done a few months ago representing quality and community, and now need to update our cards. It needs to be doubled sided, with logo and contact details on the front, and appointment details on the back. . Needs to be modern and simple, easy to read. <br/><br/>Name: Fern Vale Medical Centre <br/>Address: 512 Kestrel Rd (Cnr Kestrel Rd & Lindon Park Rd),<br/>Corvane Court Shopping Centre, Paralowie, SA 5108<br/>Ph: 08 8361 4027<br/>Tag line: Where every visit counts for you<br/>Website: www.fernvalemedicalcentre.example.au<br/>Online bookings also available<br/><br/>(On the back, to have 3 lines of appointments that can be written in.<br/>Day, date, time)<br/><br/>Your next appointment is on<br/>Can try “M T W Th F Sa Su _________________ at ____________ am/pm” or other combinations <br/>Please advise as soon as possible if unable to attend<br/>Cancellation fees apply if less than 2 hrs notice<br/>Online appointments available (please highlight this option by either by position, colour or font)

Target Market(s)

Lower social economic working class, young families to seniors

Industry/Entity Type

Medical Centre

Contact Information for Business Card

Fern Vale Medical Centre
512 Kestrel Rd (Cnr Kestrel Rd & Lindon Park Drive)
Corvane Court Shopping Centre
Marlow Heights SA 5999
Ph: 08 8361 4027
www.fernvalemedicalcentre.example.au
Tagline line: where every visit counts for you
Back side is for appointments
Your next appointment is with Dr ______________
Day/date/time (Please give 3 lines of appointments)
Please advise as soon as possible if unable to attend
Cancellation fees apply if less than 2 hours notice
Online appointments available
Book online easily and conveniently (please highlight online appointments)

Font styles to use
Serif
Sans Serif

Colors

Designer to choose colors to be used in the design.

Requirements
Must have
• Modern and simple
• Easy to ready
• Induces a wellbeing feeling
• Incorporate our logo colours and feel from logo
• Induces feeling of stability and security
Nice to have
• Attract attention
• Pleasant to look at
• Feeling of innovation
Should not have
• Loud clashing colours
• Overly luxurious feeling
• Overly artistic

```html
<!DOCTYPE html>
<html lang="en">
<head>
<meta charset="utf-8">
<title>Fern Vale Medical Centre – Business Card</title>
<link href="https://fonts.googleapis.com/css2?family=Roboto:wght@400;500;700&display=swap" rel="stylesheet">
<style>
  :root {
    --brand-blue: #1b88c9;
    --paper: #ffffff;
    --backdrop: #e4e4e4;
    --shadow: rgba(0,0,0,0.18);
  }
  * { box-sizing: border-box; margin: 0; padding: 0; }
  html, body {
    width: 1200px; height: 900px; overflow: hidden;
    background: var(--backdrop);
    font-family: "Roboto", Arial, sans-serif;
  }
  .canvas { position: relative; width: 1200px; height: 900px; }
  .card {
    position: absolute; width: 640px; height: 366px;
    background: var(--paper);
    box-shadow: 0 6px 18px var(--shadow);
    overflow: hidden; color: var(--brand-blue);
  }
  .card--appointment { left: 110px; top: 48px; }
  .card--contact { left: 450px; top: 480px; }

  .stripe { position: absolute; left: 0; right: 0; background: var(--brand-blue); }

  /* appointment side */
  .appt-title {
    position: absolute; top: 44px; left: 0; right: 0;
    text-align: center; font-size: 29px; font-weight: 500; letter-spacing: 0.3px;
  }
  .appt-band { top: 88px; height: 146px; }
  .appt-band .tagline {
    position: absolute; top: 5px; left: 0; right: 0; text-align: center;
    color: var(--paper); font-size: 17px;
  }
  .appt-band .divider { position: absolute; top: 30px; left: 0; right: 0; height: 5px; background: var(--paper); }
  .appt-lines {
    position: absolute; top: 46px; left: 70px; right: 40px;
    color: var(--paper); font-size: 18px; line-height: 30px;
  }
  .blank { display: inline-block; border-bottom: 1.5px solid var(--paper); height: 18px; vertical-align: baseline; }
  .blank--xs { width: 18px; } .blank--sm { width: 34px; } .blank--md { width: 80px; } .blank--lg { width: 150px; }
  .tick { display: inline-block; width: 10px; height: 10px; border-radius: 50%; background: var(--paper); margin: 0 2px 0 3px; }
  .appt-notice {
    position: absolute; top: 246px; left: 0; right: 0; text-align: center;
    font-size: 16px; line-height: 21px;
  }
  .online-band { top: 294px; height: 28px; }
  .online-band span {
    display: block; text-align: center; color: var(--paper);
    font-size: 18px; font-weight: 500; line-height: 28px;
  }

  /* contact side */
  .brand {
    position: absolute; top: 40px; left: 0; right: 0;
    display: flex; align-items: center; justify-content: center; gap: 10px;
  }
  .brand-dot { width: 22px; height: 22px; border-radius: 50%; background: var(--brand-blue); }
  .brand-name { font-size: 26px; font-weight: 700; color: var(--brand-blue); }
  .contact-list {
    position: absolute; top: 88px; left: 0; right: 0; text-align: center;
    font-size: 15px; line-height: 19px;
  }
  .contact-item { margin-bottom: 9px; }
  .icon { display: block; margin: 0 auto 3px; }
  .tag-band { top: 284px; height: 28px; }
  .tag-band span {
    display: block; text-align: center; color: var(--paper);
    font-size: 18px; font-weight: 500; line-height: 28px;
  }
</style>
</head>
<body>
<div class="canvas">

  <section class="card card--appointment" aria-label="Appointment side">
    <div class="stripe" style="top:20px;height:10px;"></div>
    <h1 class="appt-title">Fern Vale Medical Centre</h1>
    <div class="stripe appt-band">
      <p class="tagline">Where every visit counts for you</p>
      <div class="divider"></div>
      <div class="appt-lines">
        <p>Your next appointment is with Dr <span class="blank blank--lg"></span></p>
        <p>Day <span class="blank blank--xs"></span><span class="tick"></span>M <span class="blank blank--xs"></span><span class="tick"></span>T <span class="blank blank--xs"></span><span class="tick"></span>W <span class="blank blank--xs"></span><span class="tick"></span>Th <span class="blank blank--xs"></span><span class="tick"></span>F <span class="blank blank--xs"></span><span class="tick"></span>Sa <span class="blank blank--xs"></span><span class="tick"></span>Su</p>
        <p>Date <span class="blank blank--sm"></span>/<span class="blank blank--sm"></span>/<span class="blank blank--md"></span> Time <span class="blank blank--md"></span><span class="tick"></span>AM /<span class="tick"></span>PM</p>
      </div>
    </div>
    <p class="appt-notice">Please advise as soon as possible if unable to attend<br>(Cancellation fees apply if less than 2 hrs notice)</p>
    <div class="stripe online-band"><span>Online appointments available</span></div>
    <div class="stripe" style="top:338px;height:10px;"></div>
  </section>

  <section class="card card--contact" aria-label="Contact side">
    <div class="brand">
      <span class="brand-dot"></span>
      <span class="brand-name">Fern Vale Medical Centre</span>
    </div>
    <div class="contact-list">
      <div class="contact-item">
        <svg class="icon" width="16" height="18" viewBox="0 0 16 18" aria-hidden="true">
          <path d="M8 0C3.8 0 1 3 1 6.6 1 11 8 18 8 18s7-7 7-11.4C15 3 12.2 0 8 0z" fill="var(--brand-blue)"/>
          <circle cx="8" cy="6.5" r="2.6" fill="#fff"/>
        </svg>
        512 Kestrel Rd (Cnr Kestrel Rd &amp; Lindon Park Drive)<br>
        Corvane Court Shopping Centre<br>
        Marlow Heights SA 5999
      </div>
      <div class="contact-item">
        <svg class="icon" width="18" height="18" viewBox="0 0 18 18" aria-hidden="true">
          <circle cx="9" cy="9" r="9" fill="var(--brand-blue)"/>
          <path d="M4.5 8.5c0-2 2-3 4.5-3s4.5 1 4.5 3l-2 .3-.3-1.5H7.3L7 8.8z M6 10h6l1 3H5z" fill="#fff"/>
        </svg>
        08 8361 4027
      </div>
      <div class="contact-item">
        <svg class="icon" width="18" height="18" viewBox="0 0 18 18" aria-hidden="true">
          <circle cx="9" cy="9" r="9" fill="var(--brand-blue)"/>
          <circle cx="9" cy="9" r="5.5" fill="none" stroke="#fff" stroke-width="1.2"/>
          <ellipse cx="9" cy="9" rx="2.4" ry="5.5" fill="none" stroke="#fff" stroke-width="1"/>
          <line x1="3.5" y1="9" x2="14.5" y2="9" stroke="#fff" stroke-width="1"/>
        </svg>
        www.fernvalemedicalcentre.example.au
      </div>
    </div>
    <div class="stripe tag-band"><span>Where every visit counts for you</span></div>
    <div class="stripe" style="top:328px;height:10px;"></div>
  </section>

</div>
</body>
</html>
```